Tallowreed Advisory Partners Business Card Design

We have the logo we just need someone to design a modern business card design.

Name: Desmond Munkalt
Phone: 3055550148
Mobile: 9175550193
Web:www.tallowreedadvisory.example
email: dmunkalt@tallowreedadvisory.example
Company: Tallowreed Advisory Partners
Title: CEO

Address: 718 Quillmore Ave, Miami, Florida 33190

Target Market(s)

companies over 100 employees

Industry/Entity Type

Business

```html
<!DOCTYPE html>
<html lang="en">
<head>
<meta charset="utf-8">
<title>Tallowreed Advisory Partners – Business Card</title>
<link rel="stylesheet" href="https://fonts.googleapis.com/css2?family=Marcellus+SC&family=Montserrat:wght@400;600&display=swap">
<style>
  :root {
    --backdrop: #8b8887;
    --card: #151515;
    --card-edge: #0d0d0d;
    --ink: #f2f2f2;
    --ink-soft: #c9c9c9;
    --accent: #1f63e8;
    --accent-faint: #1a2436;
    --rule: #5a5a5a;
  }
  * { margin: 0; padding: 0; box-sizing: border-box; }
  html, body {
    width: 1200px; height: 799px; overflow: hidden;
    background: var(--backdrop);
  }
  .stage { position: relative; width: 1200px; height: 799px; }

  .card {
    position: absolute;
    background: var(--card);
    border: 1px solid var(--card-edge);
    overflow: hidden;
  }
  .card--front { left: 380px; top: 79px; width: 440px; height: 269px; }
  .card--back  { left: 388px; top: 443px; width: 424px; height: 260px; }

  .backdrop-block {
    position: absolute; left: 24px; top: 0; width: 244px; height: 269px;
    background: var(--accent-faint);
  }

  .brand {
    position: absolute; text-align: center;
    font-family: "Montserrat", sans-serif; font-weight: 600;
    color: var(--ink); text-transform: uppercase; line-height: 1.15;
  }
  .brand__dot { display: block; margin: 0 auto; border-radius: 50%; background: var(--accent); }
  .brand__name { display: block; }
  .brand__sub { display: block; }

  .card--front .brand { left: 236px; top: 51px; width: 200px; }
  .card--front .brand__dot { width: 48px; height: 48px; margin-bottom: 9px; }
  .card--front .brand__name { font-size: 15px; letter-spacing: 0.5px; }
  .card--front .brand__sub { font-size: 7px; letter-spacing: 0.6px; }

  .card--back .brand { left: 0; top: 73px; width: 424px; }
  .card--back .brand__dot { width: 74px; height: 74px; margin-bottom: 13px; }
  .card--back .brand__name { font-size: 24px; letter-spacing: 0.6px; }
  .card--back .brand__sub { font-size: 9px; letter-spacing: 1px; }

  .person { position: absolute; left: 46px; top: 128px; font-family: "Marcellus SC", serif; }
  .person__name { font-size: 15px; color: var(--ink-soft); letter-spacing: 0.6px; }
  .person__title { font-size: 11px; color: var(--accent); letter-spacing: 0.4px; }

  .divider { position: absolute; left: 46px; top: 166px; width: 354px; height: 1px; background: var(--rule); }

  .contact {
    position: absolute; left: 54px; top: 173px; list-style: none;
    font-family: "Montserrat", sans-serif; font-size: 10px; color: var(--ink-soft);
  }
  .contact li { display: flex; align-items: center; height: 15.5px; }
  .contact svg { width: 9px; height: 9px; margin-right: 15px; fill: var(--accent); }

  .address {
    position: absolute; right: 40px; top: 203px; text-align: right;
    font-family: "Montserrat", sans-serif; font-style: normal;
    font-size: 10px; line-height: 15px; color: var(--ink-soft);
  }
</style>
</head>
<body>
<main class="stage">
  <section class="card card--front">
    <div class="backdrop-block"></div>

    <div class="brand">
      <span class="brand__dot"></span>
      <span class="brand__name">Tallowreed</span>
      <span class="brand__sub">Advisory Partners</span>
    </div>

    <div class="person">
      <p class="person__name">Desmond Munkalt</p>
      <p class="person__title">CEO</p>
    </div>

    <div class="divider"></div>

    <ul class="contact">
      <li><svg viewBox="0 0 10 10"><path d="M1 3c0-1 1-2 4-2s4 1 4 2v1H7V3H3v1H1zM2 5h6l1 4H1z"/></svg>305-555-0148</li>
      <li><svg viewBox="0 0 10 10"><path d="M3 0.5h4v9H3z"/></svg>917-555-0193</li>
      <li><svg viewBox="0 0 10 10"><path d="M1 2h8v6H1zM1.5 2.5 5 5.5 8.5 2.5" stroke="#151515" stroke-width="0.8"/></svg>dmunkalt@tallowreedadvisory.example</li>
      <li><svg viewBox="0 0 10 10"><circle cx="5" cy="5" r="4"/><path d="M1 5h8M5 1v8" stroke="#151515" stroke-width="0.7"/></svg>www.tallowreedadvisory.example</li>
    </ul>

    <address class="address">
      718 Quillmore Ave<br>Miami, Florida 33190
    </address>
  </section>

  <section class="card card--back">
    <div class="brand">
      <span class="brand__dot"></span>
      <span class="brand__name">Tallowreed</span>
      <span class="brand__sub">Advisory Partners</span>
    </div>
  </section>
</main>
</body>
</html>
```